Helicopter Company - Rotavia Sweden

I need a new design and implementation of a webpage. We rent helicopters and are also starting a school. We havre started a wordpress but the page is very ugly. Need a complete update. Logo exist already. We also have some pictures of helicotopers. We are open for all designs but it is important that it looks professionel, is eassy to update and will give an impression och structure and dicipline.
Updates

Target Market(s)

Customers that what to get a certificate to fly. It is expensive so it’s either people with a lot of money or people with a big dream. It is very serious business.

Industry/Entity Type

www.rotavia-demo.se

Coding

Coded - Design and coding required

Number of Pages Required

4 page

Font styles to use
Sans Serif

Colors
0054AA
0677BA
7BADD7
CADEEF
E8F1F8

Requirements
Must have
• A easy page the gives a feeling of seriousness and

```html
<!DOCTYPE html>
<html lang="sv">
<head>
<meta charset="utf-8">
<title>Rotavia Sweden AB</title>
<link href="https://fonts.googleapis.com/css2?family=Montserrat:wght@500;600;700;800;900&family=Mulish:wght@400;500;600&display=swap" rel="stylesheet">
<style>
:root{
  --blue:#0677ff;
  --blue-deep:#0054aa;
  --blue-light:#7badd7;
  --blue-pale:#cadeef;
  --blue-mist:#e8f1f8;
  --ink:#1c1c1c;
  --text:#3d3d3d;
  --grey-bg:#efefef;
  --footer:#2b2b2b;
  --white:#ffffff;
}
*{margin:0;padding:0;box-sizing:border-box}
html,body{width:1200px;height:3335px;overflow:hidden}
body{position:relative;font-family:'Mulish',sans-serif;color:var(--text);background:var(--white)}
.abs{position:absolute}
.btn{position:absolute;display:flex;align-items:center;justify-content:center;background:var(--blue);color:var(--white);font-family:'Montserrat',sans-serif;font-weight:800;font-size:11px;border-radius:6px;letter-spacing:.2px}
.rule{position:absolute;height:3px;background:var(--blue)}
h1,h2,h3{font-family:'Montserrat',sans-serif}

/* hero */
.hero{position:absolute;left:0;top:0;width:1200px;height:633px;background:linear-gradient(180deg,#7d86a6 0%,#c99a8e 25%,#f2b27f 42%,#b98263 58%,#3c4a2e 75%,#2d3b2a 100%)}
.logo{position:absolute;font-family:'Mulish',sans-serif;font-weight:500;letter-spacing:1px;color:var(--ink)}
.nav{position:absolute;top:35px;left:485px;display:flex;align-items:center;gap:24px;font-family:'Montserrat',sans-serif;font-size:13px;font-weight:500;color:var(--ink)}
.nav .active{background:var(--blue);color:var(--white);padding:5px 9px;border-radius:5px;font-weight:700}
.contact-item{display:flex;align-items:center;gap:8px;font-family:'Mulish',sans-serif;font-size:15px;margin-left:6px}
.hero-title{position:absolute;left:781px;top:134px;font-size:42px;line-height:52px;font-weight:900;color:var(--white);text-shadow:0 2px 8px rgba(90,50,40,.45)}
.dots{position:absolute;left:572px;top:578px;display:flex;gap:7px}
.dots span{width:11px;height:11px;border-radius:50%;border:2px solid var(--white)}
.dots .on{background:var(--blue);box-shadow:0 0 0 2px var(--white) inset}

/* welcome */
.welcome-kicker{left:135px;top:702px;font-size:18px;font-weight:600;color:var(--ink);font-family:'Montserrat',sans-serif}
.welcome-title{left:134px;top:731px;font-size:24px;font-weight:900;color:var(--ink)}
.welcome-title span{color:var(--blue)}
.body-copy{font-size:13.5px;line-height:22.4px;color:var(--text)}

/* fleet */
.fleet{position:absolute;left:0;top:1130px;width:1200px;height:576px;background:var(--grey-bg)}
.section-title{position:absolute;width:100%;text-align:center;top:41px;font-size:20px;font-weight:800;color:var(--ink)}
.section-title span{color:var(--blue)}
.card{position:absolute;top:123px;width:300px;height:410px;background:var(--white);border-radius:6px;box-shadow:0 2px 10px rgba(0,0,0,.06);overflow:hidden;text-align:center}
.card-photo{height:236px}
.card h3{margin-top:26px;font-size:14px;font-weight:700;color:var(--ink)}
.card p{margin:14px auto 0;width:230px;font-size:13.5px;line-height:20px}
.card .btn{left:110px;top:350px;width:79px;height:27px;font-size:10.5px}

/* hire band */
.hire{position:absolute;left:0;top:1706px;width:1200px;height:387px;background:linear-gradient(180deg,#7a93b3 0%,#9fb2c9 45%,#c1cad3 68%,#6f7f55 80%,#76884c 100%)}
.band-title{left:132px;top:62px;font-size:19px;font-weight:800;color:var(--white)}
.band-copy{left:132px;top:120px;width:445px;font-size:16px;line-height:22.3px;color:var(--white)}

/* school */
.school-shadow{left:143px;top:2148px;width:500px;height:377px;background:var(--blue-mist);border-radius:4px}
.school-photo{left:133px;top:2138px;width:499px;height:377px;border-radius:4px;background:linear-gradient(160deg,#4a3c34 0%,#8b8b8c 40%,#b7c2c8 55%,#6d6a66 75%,#2f2b28 100%)}
.school-title{left:691px;top:2160px;font-size:20px;font-weight:800;color:var(--blue)}

/* other jobs */
.jobs{position:absolute;left:0;top:2567px;width:1200px;height:418px;background:linear-gradient(180deg,#2f6fd1 0%,#86b4ec 32%,#c7dbee 45%,#4f7a39 58%,#6e9c3e 80%,#88ad4a 100%)}
.jobs-card{position:absolute;left:132px;top:62px;width:353px;height:286px;background:rgba(255,255,255,.95);border-radius:6px}
.jobs-card h2{position:absolute;left:38px;top:36px;font-size:19px;line-height:28px;font-weight:700;color:var(--ink)}
.jobs-card p{position:absolute;left:39px;top:104px;width:280px;font-size:14px;line-height:20.7px}

/* footer */
.footer{position:absolute;left:0;top:2985px;width:1200px;height:350px;background:var(--footer);color:var(--white)}
.footer h4{position:absolute;top:44px;font-family:'Montserrat',sans-serif;font-size:12.5px;font-weight:700;letter-spacing:.3px}
.f-row{position:absolute;display:flex;align-items:center;gap:11px;font-size:12px;line-height:15px}
.f-icon{width:22px;height:22px;border-radius:50%;background:var(--white);display:flex;align-items:center;justify-content:center;flex-shrink:0}
.f-menu{position:absolute;left:733px;top:77px;font-size:12px;line-height:24px;letter-spacing:.2px}
.f-divider{position:absolute;left:132px;top:258px;width:936px;height:1px;background:#3c3c3c}
.copyright{position:absolute;width:100%;top:297px;text-align:center;font-size:11px}
</style>
</head>
<body>

<header class="hero" role="img" aria-label="Helikopter som flyger över en flod och skogklädda öar vid solnedgång">
  <div class="logo" style="left:132px;top:38px;font-size:28px;">ROTAVIA</div>
  <nav class="nav">
    <span class="active">START</span>
    <span>OM OSS</span>
    <span>KONTAKT</span>
    <span class="contact-item">
      <svg width="22" height="22" viewBox="0 0 24 24" fill="none" stroke="#1c1c1c" stroke-width="1.6"><circle cx="12" cy="12" r="11"/><path d="M8.5 6.5l2 2.5-1.2 1.4c.8 1.7 2 2.9 3.8 3.8l1.4-1.2 2.5 2-1.1 1.8c-4.6-.4-8.6-4.4-9-9z"/></svg>
      +46 700 123 456
    </span>
    <span class="contact-item">
      <svg width="22" height="22" viewBox="0 0 24 24" fill="none" stroke="#1c1c1c" stroke-width="1.6"><circle cx="12" cy="12" r="11"/><rect x="6.5" y="8" width="11" height="8" rx="1"/><path d="M6.5 8.5l5.5 4 5.5-4"/></svg>
      info@rotavia-demo.se
    </span>
  </nav>
  <h1 class="hero-title">HYR DIN<br>HELIKOPTER<br>AV OSS!</h1>
  <div class="btn" style="left:781px;top:305px;width:205px;height:46px;font-size:17px;border-radius:7px;box-shadow:0 3px 8px rgba(0,0,0,.2)">LÄS MER OM OSS</div>
  <div class="dots"><span></span><span class="on"></span><span></span><span></span></div>
</header>

<section class="welcome">
  <div class="abs welcome-kicker">VÄLKOMMEN TILL</div>
  <h2 class="abs welcome-title"><span>ROTAVIA</span> SWEDEN AB.</h2>
  <div class="rule" style="left:135px;top:778px;width:123px"></div>
  <p class="abs body-copy" style="left:134px;top:819px;width:390px">Rotavia startades med visionen att göra helikopterflygning mer tillgänglig i södra Sverige. Att flyga helikopter i sverige är oftast ganska kostsamt och svårt med tillgänglighet. Detta medför att många som har certifikat ofta får vänta länge mellan sina flygningar. Vi vill förbättra tillgängligheten och serviecen framförallt med helikopterhyra i skåne och i södra Sverige.</p>
  <div class="btn" style="left:135px;top:1010px;width:88px;height:30px">LÄS MER</div>
  <svg class="abs" style="left:600px;top:650px" width="470" height="450" viewBox="0 0 470 450">
    <circle cx="228" cy="230" r="223" fill="var(--blue-mist)"/>
  </svg>
  <div class="abs" role="img" aria-label="Två helikoptrar, en i luften och en på en grön gräsplan" style="left:632px;top:664px;width:424px;height:424px;border-radius:50%;background:linear-gradient(180deg,#8fb6dc 0%,#c4d8e8 45%,#6f9a4a 55%,#4d8a2a 100%)"></div>
</section>

<section class="fleet">
  <h2 class="section-title"><span>VÅRA</span> HELIKOPTRAR!</h2>
  <div class="rule" style="left:582px;top:80px;width:36px"></div>
  <article class="card" style="left:132px">
    <div class="card-photo" role="img" aria-label="Mörkblå helikopter på en gräsplan framför skog" style="background:linear-gradient(180deg,#4f86c9 0%,#a8c3df 35%,#3f5a2e 55%,#7c8f4a 100%)"></div>
    <h3>ROTOR R40</h3>
    <p>Rotor R40 är en av världens mest använda helikoptrar.</p>
    <div class="btn">LÄS MER</div>
  </article>
  <article class="card" style="left:450px">
    <div class="card-photo" role="img" aria-label="Helikopter parkerad på asfalt vid ett staket" style="background:linear-gradient(180deg,#6f9fd6 0%,#bcd0e2 40%,#6c6e70 60%,#8b8d8f 100%)"></div>
    <h3>FALK 1</h3>
    <p>När du hyr helikopter av oss kan du välja en superfin Falk 1</p>
    <div class="btn">LÄS MER</div>
  </article>
  <article class="card" style="left:769px">
    <div class="card-photo" role="img" aria-label="Helikopter inne i en hangar" style="background:linear-gradient(180deg,#8a8c8e 0%,#4c4d4f 45%,#2a2b2d 70%,#707274 100%)"></div>
    <h3>KESTREL 2.</h3>
    <p>Hos oss kan du hyra helikopter Rotor Kestrel 2.</p>
    <div class="btn">LÄS MER</div>
  </article>
</section>

<section class="hire" role="img" aria-label="Helikopter som lyfter från ett flygfält under en molnig himmel">
  <h2 class="abs band-title">HYR HELIKOPTER AV OSS!</h2>
  <div class="abs" style="left:132px;top:90px;width:41px;height:3px;background:var(--white)"></div>
  <p class="abs band-copy">Hos oss kan ni hyra helikopter i skåne. Egentligen kan ni hyra den var som helst och vi har till och med leverans av helikopter. Vill ni ha den framflygen står vi för piloten och hens transport samt logi. Du står bara för själva kostnaden av helikoptern.</p>
  <div class="btn" style="left:133px;top:253px;width:87px;height:31px">LÄS MER</div>
</section>

<section class="school">
  <div class="abs school-shadow"></div>
  <div class="abs school-photo" role="img" aria-label="Elev och pilot i en helikopterkabin med utsikt över en stad"></div>
  <h2 class="abs school-title">SKOLA</h2>
  <div class="rule" style="left:691px;top:2201px;width:70px"></div>
  <p class="abs body-copy" style="left:691px;top:2242px;width:382px">There are many variations of passages of Lorem Ipsum available, but the majority have suffered alteration in some form, by injected humour, or randomised words which don't look even slightly believable. If you are going to use a passage of Lorem Ipsum, you need to be sure there isn't anything embarrassing hidden in the middle of text. All the Lorem Ipsum generators on the Internet tend to repeat predefined chunks as necessary</p>
  <div class="btn" style="left:694px;top:2457px;width:87px;height:31px">LÄS MER</div>
</section>

<section class="jobs" role="img" aria-label="Mörkblå helikopter på en gräsplan under blå himmel">
  <div class="jobs-card">
    <h2>ANDRA TYPER AV<br>HELIKOPTERJOBB</h2>
    <p>Genom samarbeten med andra aktörer kan vi med våra maskiner utgå från södra Sverige och utföra diverse arbeten. Detta sparar stora transferkostnader för helikoptern.</p>
    <div class="btn" style="left:39px;top:225px;width:87px;height:30px">LÄS MER</div>
  </div>
</section>

<footer class="footer">
  <div class="logo" style="left:132px;top:100px;font-size:32px;color:var(--white)">ROTAVIA</div>

  <h4 style="left:437px">KONTAKTA OSS</h4>
  <div class="f-row" style="left:437px;top:78px">
    <span class="f-icon"><svg width="11" height="12" viewBox="0 0 12 14"><path d="M6 0a5 5 0 0 1 5 5c0 3.5-5 9-5 9S1 8.5 1 5a5 5 0 0 1 5-5z" fill="#2b2b2b"/><circle cx="6" cy="5" r="1.8" fill="#fff"/></svg></span>
    <span>Rotavia,<br>Norrvik Flygfält,</span>
  </div>
  <div class="f-row" style="left:437px;top:129px">
    <span class="f-icon"><svg width="11" height="11" viewBox="0 0 12 12"><path d="M2 1l2.2 2.6-1 1.3c.8 1.6 2 2.8 3.7 3.7l1.3-1L11 9.8 9.8 11.5C5.3 11 1 6.7.5 2.2z" fill="#2b2b2b"/></svg></span>
    <span>Ring oss<br>+46 (0) 707 123 456</span>
  </div>
  <div class="f-row" style="left:437px;top:181px">
    <span class="f-icon"><svg width="11" height="9" viewBox="0 0 12 9"><rect width="12" height="9" rx="1" fill="#2b2b2b"/><path d="M0.5 1l5.5 4 5.5-4" stroke="#fff" fill="none"/></svg></span>
    <span>Mejla oss<br>info@rotavia-demo.se</span>
  </div>

  <h4 style="left:733px">MENY</h4>
  <div class="f-menu">START<br>OM OSS<br>KONTAKT</div>

  <h4 style="left:970px">FÖLJ OSS</h4>
  <div class="f-row" style="left:968px;top:77px"><span class="f-icon"></span><span>Like us on<br>FRIENDLINE</span></div>
  <div class="f-row" style="left:968px;top:128px"><span class="f-icon"></span><span>Follow us on<br>CHIRPER</span></div>
  <div class="f-row" style="left:968px;top:178px"><span class="f-icon"></span><span>Follow us on<br>WORKNET</span></div>

  <div class="f-divider"></div>
  <div class="copyright">Copyright © 2023 All Rights Reserved</div>
</footer>

</body>
</html>
```